KRT business cards

I need a Business card design for my self. I am behavior analyst owner of a new company based in Miami. We offer Applied Behavior Analysis (ABA) services to individuals with developmental disabilities.

Business

```html
<!DOCTYPE html>
<html lang="en">
<head>
<meta charset="utf-8">
<title>KRT business cards</title>
<link href="https://fonts.googleapis.com/css2?family=Cinzel:wght@600&family=Arimo:wght@400&display=swap" rel="stylesheet">
<style>
  :root {
    --navy: #0d4a85;
    --green: #5aa83c;
    --white: #ffffff;
    --page: #ece9e4;
  }
  html, body { margin: 0; padding: 0; overflow: hidden; }
  body {
    width: 1200px; height: 1024px;
    background: var(--page);
    font-family: "Arimo", Arial, sans-serif;
    position: relative;
  }
  .card {
    position: absolute; left: 215px;
    width: 770px; height: 440px;
    background: var(--white);
    border-radius: 28px;
    overflow: hidden;
    box-shadow: 0 6px 18px rgba(0,0,0,.18);
  }
  .card--front { top: 48px; }
  .card--back { top: 536px; }

  .brand { display: flex; align-items: center; gap: 22px; position: absolute; }
  .brand__name {
    font-family: "Cinzel", "Times New Roman", serif;
    font-weight: 600; color: var(--navy);
    letter-spacing: 6px; line-height: 1;
  }
  .brand__dot { border-radius: 50%; background: var(--green); }

  .card--front .brand { left: 60px; top: 60px; }
  .card--front .brand__name { font-size: 92px; }
  .card--front .brand__dot { width: 34px; height: 34px; }

  .contact-band {
    position: absolute; left: 0; right: 0; bottom: 0; height: 215px;
    background: var(--navy);
  }
  .contact-band__tab {
    position: absolute; left: 0; top: 0; width: 18px; height: 100%;
    background: var(--green);
  }
  .contact { position: absolute; left: 60px; top: 30px; color: var(--white); }
  .contact__name { font-size: 30px; margin: 0 0 4px; font-weight: 400; }
  .contact__title { font-size: 16px; color: var(--green); margin: 0 0 14px; }
  .contact__row { display: flex; align-items: center; gap: 12px; font-size: 22px; margin-bottom: 8px; }
  .contact__row svg { width: 20px; height: 20px; flex: none; }

  .card--back .brand { left: 0; right: 0; top: 95px; justify-content: center; }
  .card--back .brand__name { font-size: 64px; }
  .card--back .brand__dot { width: 26px; height: 26px; }

  .services-band {
    position: absolute; left: 0; right: 0; top: 230px; height: 110px;
    background: var(--navy);
    color: var(--white);
    display: flex; flex-direction: column; justify-content: center; align-items: center;
    font-size: 24px; line-height: 1.5;
  }
  .services-band .sep { color: var(--green); padding: 0 8px; }
  .website { position: absolute; left: 0; right: 0; top: 365px; text-align: center; color: var(--navy); font-size: 22px; }
</style>
</head>
<body>

<section class="card card--front" aria-label="Business card front">
  <div class="brand">
    <span class="brand__name">KRT</span>
    <span class="brand__dot"></span>
  </div>
  <div class="contact-band">
    <div class="contact-band__tab"></div>
    <div class="contact">
      <p class="contact__name">Marisol Ortega, B.A.</p>
      <p class="contact__title">Board Certified Asst. Behavior Analyst (BCABA)</p>
      <div class="contact__row">
        <svg viewBox="0 0 20 20"><path fill="#fff" d="M5 2l3 4-2 2c1 2 3 4 5 5l2-2 4 3-2 4C8 17 3 12 2 4z"/></svg>
        <span>305-555-0142</span>
      </div>
      <div class="contact__row">
        <svg viewBox="0 0 20 20"><rect x="2" y="4" width="16" height="12" fill="#fff"/><path d="M2 4l8 7 8-7" fill="none" stroke="#0d4a85" stroke-width="1.6"/></svg>
        <span>m.ortega.aba@mail.com</span>
      </div>
      <div class="contact__row">
        <svg viewBox="0 0 20 20"><circle cx="10" cy="10" r="8" fill="none" stroke="#fff" stroke-width="1.8"/><path d="M2 10h16M10 2c-4 4-4 12 0 16M10 2c4 4 4 12 0 16" fill="none" stroke="#fff" stroke-width="1.4"/></svg>
        <span>www.krtaba.com</span>
      </div>
    </div>
  </div>
</section>

<section class="card card--back" aria-label="Business card back">
  <div class="brand">
    <span class="brand__name">KRT</span>
    <span class="brand__dot"></span>
  </div>
  <div class="services-band">
    <div>Applied Behavior Analysis<span class="sep">|</span>Parent/Teacher Training</div>
    <div>Social Skills Training<span class="sep">|</span>Tutoring</div>
  </div>
  <div class="website">www.krtaba.com</div>
</section>

</body>
</html>
```